USB Business Card Design
Pelham Trowbridge Partners Chartered Accountants
Simple
Marcus Trowbridge, CA
Partner
20418-127 Ave
Edmonton, AB
T6K 4M3
T:855.316.2084
P:780.316.2084, D: 780.552.7391
F:780.317.6058
MTrowbridge@ptpca.com
www.ptpca.com
This is going to be printed onto a Business card sized USB stick. They are 2 sided, flashy and plastic coated. This is for extremely high end clients and need to look really amazing! We are open to all ideas, the bosses are partial to a simple look.

```html
<!DOCTYPE html>
<html lang="en">
<head>
<meta charset="utf-8">
<title>Pelham Trowbridge Partners – Business Card</title>
<link href="https://fonts.googleapis.com/css2?family=Questrial&display=swap" rel="stylesheet">
<style>
  :root {
    --backdrop: #2a2a2c;
    --silver-light: #fbfbfc;
    --silver-mid: #e6e7ea;
    --silver-dark: #cfd1d6;
    --blue-deep: #0d2a78;
    --blue-main: #1f4fb8;
    --blue-bright: #3d74dc;
    --ink-blue: #1d3f9a;
    --ink-grey: #7c8088;
    --ink-white: #ffffff;
    --ink-soft: #d6e1fa;
  }
  * { box-sizing: border-box; margin: 0; padding: 0; }
  html, body {
    width: 1200px; height: 901px; overflow: hidden;
    background: var(--backdrop);
    font-family: "Questrial", "Century Gothic", sans-serif;
  }
  .sheet {
    width: 1200px; height: 901px;
    display: flex; flex-direction: column; align-items: center; justify-content: center;
    gap: 34px;
  }
  .card {
    position: relative;
    width: 720px; height: 410px;
    border-radius: 6px;
    overflow: hidden;
    background: linear-gradient(170deg, var(--silver-light) 0%, var(--silver-mid) 60%, var(--silver-dark) 100%);
    box-shadow: 0 10px 28px rgba(0,0,0,0.55);
  }
  .band {
    position: absolute; left: 0; right: 0;
    background: linear-gradient(180deg, var(--blue-bright) 0%, var(--blue-main) 35%, var(--blue-deep) 100%);
  }
  .band::after {
    content: ""; position: absolute; inset: 0;
    background: linear-gradient(100deg, rgba(255,255,255,0.18) 0%, rgba(255,255,255,0) 45%, rgba(255,255,255,0.08) 75%, rgba(255,255,255,0) 100%);
  }
  .wordmark { display: flex; align-items: center; gap: 12px; }
  .wordmark__square { width: 18px; height: 18px; }
  .wordmark__name { font-size: 25px; letter-spacing: 0.5px; }

  /* back face */
  .card--back .band { top: 170px; height: 150px; }
  .card--back .alt-mark { position: absolute; top: 62px; left: 0; right: 0; display: flex; justify-content: center; }
  .card--back .alt-mark .wordmark__name { color: var(--ink-blue); font-size: 30px; }
  .card--back .alt-mark .wordmark__square { background: var(--ink-blue); }
  .card--back .band-mark { position: absolute; top: 222px; left: 70px; z-index: 1; }
  .card--back .band-mark .wordmark__name { color: var(--ink-white); }
  .card--back .band-mark .wordmark__square { background: var(--ink-white); }
  .card--back .web { position: absolute; right: 34px; top: 336px; font-size: 13px; letter-spacing: 3px; color: var(--ink-grey); }

  /* front face */
  .card--front .band { top: 128px; height: 226px; }
  .card--front .top-mark { position: absolute; top: 48px; left: 44px; }
  .card--front .top-mark .wordmark__name { color: var(--ink-blue); }
  .card--front .top-mark .wordmark__square { background: var(--ink-blue); }
  .contact { position: absolute; top: 146px; left: 44px; z-index: 1; color: var(--ink-white); font-size: 15px; line-height: 20px; }
  .contact__address { margin-bottom: 12px; color: var(--ink-soft); }
  .contact__row { display: flex; align-items: center; gap: 10px; }
  .contact__row svg { width: 14px; height: 14px; fill: var(--ink-white); flex: none; }
  .signature { position: absolute; right: 56px; top: 280px; z-index: 1; color: var(--ink-white); }
  .signature__name { font-size: 21px; }
  .signature__title { font-size: 14px; color: var(--ink-soft); margin-top: 2px; }
  .card--front .web { position: absolute; left: 44px; bottom: 20px; font-size: 13px; letter-spacing: 3px; color: var(--ink-grey); }
</style>
</head>
<body>
<main class="sheet">

  <section class="card card--back" aria-label="Card back">
    <div class="alt-mark wordmark">
      <span class="wordmark__square"></span>
      <span class="wordmark__name">Northvale Capital</span>
    </div>
    <div class="band"></div>
    <div class="band-mark wordmark">
      <span class="wordmark__square"></span>
      <span class="wordmark__name">Pelham Trowbridge Partners</span>
    </div>
    <p class="web">www.ptpca.com</p>
  </section>

  <section class="card card--front" aria-label="Card front">
    <div class="top-mark wordmark">
      <span class="wordmark__square"></span>
      <span class="wordmark__name">Pelham Trowbridge Partners</span>
    </div>
    <div class="band"></div>
    <div class="contact">
      <p class="contact__address">20418-127 Ave<br>Edmonton, AB<br>T6K 4M3</p>
      <p class="contact__row">
        <svg viewBox="0 0 16 16" aria-hidden="true"><path d="M3 1h3l1.5 4-2 1.3a9 9 0 0 0 4.2 4.2L11 8.5l4 1.5v3a2 2 0 0 1-2 2A12 12 0 0 1 1 3a2 2 0 0 1 2-2z"/></svg>
        855.316.2084
      </p>
      <p class="contact__row">
        <svg viewBox="0 0 16 16" aria-hidden="true"><path d="M4 0h6v2H4zM5 3h6v12H5zM3 3h1v12H3zM12 5h1v2h-1z"/></svg>
        780.316.2084, D: 780.552.7391
      </p>
      <p class="contact__row">
        <svg viewBox="0 0 16 16" aria-hidden="true"><path d="M4 1h8v4H4zM1 6h14v6h-3v3H4v-3H1zM5 10v4h6v-4z"/></svg>
        780.317.6058
      </p>
      <p class="contact__row">
        <svg viewBox="0 0 16 16" aria-hidden="true"><path d="M1 3h14v10H1zM2 4.2v.4l6 4.2 6-4.2v-.4z"/></svg>
        MTrowbridge@ptpca.com
      </p>
    </div>
    <div class="signature">
      <p class="signature__name">Marcus Trowbridge, CA</p>
      <p class="signature__title">Partner</p>
    </div>
    <p class="web">www.ptpca.com</p>
  </section>

</main>
</body>
</html>
```